Fashion Design Business Card

I need a new business card designed for a new fashion company. I have attached what I have currently designed. I want it more feminine looking, the logo needs to be gold. I want it simple, feminine and stylish. Please give me some different ideas with the fonts.

I need to send the design we currently have, as we have worked out the logo.
You also need all of our details
Fashion

```html
<!DOCTYPE html>
<html lang="en">
<head>
<meta charset="utf-8">
<title>Marina Ellwood – Business Card</title>
<link rel="stylesheet" href="https://fonts.googleapis.com/css2?family=Josefin+Sans:wght@300;400&family=Courgette&family=Lato:wght@400&display=swap">
<style>
  :root {
    --page-bg: #ececec;
    --card-black: #050505;
    --card-red-top: #d93333;
    --card-red-mid: #8c1c1c;
    --card-red-bottom: #3a0808;
    --gold: #e0aa2a;
    --name-copper: #c8825e;
    --tagline-orange: #d9782f;
    --contact-grey: #a9a9a9;
    --ghost: rgba(255, 255, 255, 0.045);
  }
  * { margin: 0; padding: 0; box-sizing: border-box; }
  html, body {
    width: 1200px;
    height: 900px;
    overflow: hidden;
    background: var(--page-bg);
  }
  .canvas {
    position: relative;
    width: 1200px;
    height: 900px;
  }
  .card {
    position: absolute;
    top: 293px;
    width: 560px;
    height: 314px;
    border-radius: 16px;
    overflow: hidden;
  }
  .card--front {
    left: 38px;
    background: var(--card-black);
  }
  .card--back {
    left: 620px;
    background: linear-gradient(180deg, var(--card-red-top) 0%, var(--card-red-mid) 50%, var(--card-red-bottom) 100%);
  }
  .ghost-mark {
    position: absolute;
    left: 20px;
    top: 20px;
    width: 330px;
    height: 330px;
    border-radius: 50%;
    background: var(--ghost);
  }
  .brand-mark {
    position: absolute;
    display: flex;
    align-items: center;
    gap: 8px;
    font-family: "Josefin Sans", sans-serif;
    font-weight: 400;
    color: var(--gold);
    white-space: nowrap;
  }
  .card--front .brand-mark {
    left: 40px;
    top: 88px;
    font-size: 15px;
  }
  .brand-mark__dot {
    width: 12px;
    height: 12px;
    border-radius: 50%;
    background: var(--gold);
  }
  .card--back .brand-mark {
    left: 0;
    right: 0;
    top: 138px;
    justify-content: center;
    font-size: 30px;
    gap: 12px;
  }
  .card--back .brand-mark__dot {
    width: 20px;
    height: 20px;
  }
  .identity {
    position: absolute;
    left: 208px;
    top: 60px;
  }
  .identity__name {
    font-family: "Josefin Sans", sans-serif;
    font-weight: 300;
    font-size: 27px;
    letter-spacing: 1px;
    color: var(--name-copper);
    text-transform: uppercase;
    word-spacing: 6px;
  }
  .identity__role {
    margin: 6px 0 0 76px;
    font-family: "Courgette", cursive;
    font-size: 16px;
    color: var(--tagline-orange);
  }
  .contact {
    position: absolute;
    left: 261px;
    top: 222px;
    list-style: none;
    font-family: "Lato", sans-serif;
    font-size: 15px;
    line-height: 22px;
    color: var(--contact-grey);
  }
</style>
</head>
<body>
<main class="canvas">
  <section class="card card--front" aria-label="Card front">
    <div class="ghost-mark" aria-hidden="true"></div>
    <div class="brand-mark">
      <span class="brand-mark__dot"></span>
      <span>Marina Ellwood</span>
    </div>
    <div class="identity">
      <h1 class="identity__name">Marina Ellwood</h1>
      <p class="identity__role">fashion designer</p>
    </div>
    <ul class="contact">
      <li>PHONE: 0400 555 318</li>
      <li>Email:&nbsp; marina@marinaellwood.com</li>
      <li>Web:&nbsp; www.marinaellwood.com</li>
    </ul>
  </section>

  <section class="card card--back" aria-label="Card back">
    <div class="brand-mark">
      <span class="brand-mark__dot"></span>
      <span>Marina Ellwood</span>
    </div>
  </section>
</main>
</body>
</html>
```